Valdora event looking for a creative flyer design

I am looking for a creative flyer design for an event going on Tuesday, October 25th at 4 pm in the Halvorsen Auditorium, Drexmoor Center for Applied Discovery, 1872 Larkwell Terrace, Philadelphia, PA 19104. The name of the seminar is Mapping the Mindscape, and it will feature five speakers: Professors Nadine Forsyth, Tomas Welling, Patrick Ellery, Gordon Huxley, and Colin Tavish. Provost Harold Quimby will make the welcome introduction. The seminar will include a panel discussion at the end of the event and a reception following that in the Drexmoor Lobby. For questions about this event, please put my contact information on the flyer: Marta Lindqvist-Okafor / O: 215-555-0147 / mlok@valdora-univ.example.
I would like to have everyone's picture on the flyer with their titles listed below, and the Logo for the program should be placed on the flyer as well. Also, if more background would be helpful in creating the flyer, please go to the VCX (Valdora Connects Expertise) Program website at https://vcxfaculty.valdora-univ.example. I would also like to include a QR code on the flyer to link to the VCX internet site.
Doing the Welcome Address:
Harold Quimby
Warren K. Dobbins Professor of Communication in the Feldkamp School for Communication and Professor of Political Science in the School of Arts & Sciences
The Speakers are:
Nadine T. Forsyth
Lewis G. Harlan University Professor (Epigenetics + Biology)
Tomas Welling
Corinne Fairley University Professor (Mathematics + Systems Engineering)
Patrick R. Ellery
Martin and Ruth Abelard University Professor (History + Bioethics)
Gordon W. Huxley
Thomas E. Wyndel University Professor (Neuroscience + Psychology + Marketing)
Colin Tavish
Edwin Coyle University Professor (Criminology + Psychiatry + Psychology)
Lastly, I would also like to create a digital evite version of the flyer with some pop-up or music/commentary to it. It can have a little more information like maybe include the tabs (about the program, meet the professors, inclusion, innovation, impact) from the VCX website someplace so that people can read more about the program and the professors.
I will also need to create an invite for lunch the next day with the speakers, but can discuss more once we start working on the seminar flyer. Please contact me with any questions.
I am working on getting a better quality logo image.

```html
<!DOCTYPE html>
<html lang="en">
<head>
<meta charset="utf-8">
<title>Mapping the Mindscape — Seminar Flyer</title>
<link rel="stylesheet" href="https://fonts.googleapis.com/css2?family=Alfa+Slab+One&family=Arimo:wght@700&family=Nunito:wght@800&family=PT+Sans:wght@400&family=Tinos:wght@700&display=swap">
<style>
  :root {
    --navy: #1b2a3c;
    --title-navy: #1a2740;
    --sky: #2f9bd6;
    --header-grey: #c9c9c9;
    --gold: #f6e24c;
    --white: #ffffff;
    --ink: #111111;
    --page-bg: #e6e6e6;
  }
  * { box-sizing: border-box; margin: 0; padding: 0; }
  html, body { width: 1200px; height: 1200px; overflow: hidden; background: var(--page-bg); }
  .stage { position: relative; width: 1200px; height: 1200px; }
  .flyer-frame { position: absolute; left: 175px; top: 0; width: 849px; height: 1200px; overflow: hidden; }
  .flyer {
    position: absolute; left: 0; top: 0; width: 900px; height: 1272px;
    transform: scale(0.9434); transform-origin: 0 0;
    background: var(--white); font-family: "PT Sans", sans-serif; color: var(--ink);
  }
  .top-rule { position: absolute; left: 0; top: 0; width: 900px; height: 5px; background: var(--sky); }
  .header { position: absolute; left: 0; top: 5px; width: 900px; height: 320px; }
  .header svg { position: absolute; inset: 0; }
  .title {
    position: absolute; left: 40px; top: 22px; width: 500px; text-align: center;
    font-family: "Alfa Slab One", serif; color: var(--title-navy);
    font-size: 84px; line-height: 92px;
    -webkit-text-stroke: 10px var(--white); paint-order: stroke fill;
    filter: drop-shadow(3px 4px 3px rgba(0,0,0,.35));
  }
  .band { position: absolute; left: 0; top: 325px; width: 900px; height: 98px; background: var(--sky); }
  .band-details {
    position: absolute; left: 20px; top: 4px; width: 520px; text-align: center;
    font-family: "Nunito", sans-serif; font-weight: 800; font-size: 22px; line-height: 29.5px;
    color: var(--gold); -webkit-text-stroke: 3px var(--navy); paint-order: stroke fill;
  }
  .host { position: absolute; left: 570px; top: 4px; width: 310px; color: var(--white); }
  .host-name { font-family: "Arimo", sans-serif; font-size: 19px; text-align: center; line-height: 26px; }
  .host-role { font-size: 14.5px; line-height: 19.5px; text-align: justify; text-align-last: justify; margin-top: 2px; }
  .host-role span { display: block; text-align: justify; text-align-last: justify; }
  .photo {
    position: absolute; border: 2px solid var(--sky); border-radius: 3px; width: 250px;
  }
  .speaker-name { position: absolute; width: 300px; text-align: center; font-family: "Arimo", sans-serif; font-size: 18px; }
  .speaker-role { position: absolute; width: 300px; text-align: center; font-size: 13.5px; line-height: 18px; }
  .feature-note {
    position: absolute; left: 326px; top: 515px; width: 250px; text-align: center;
    font-family: "Tinos", serif; font-size: 29px; line-height: 38.5px; color: var(--ink);
  }
  .footer-rule { position: absolute; left: 0; top: 1163px; width: 900px; height: 15px; background: var(--sky); }
  .footer { position: absolute; left: 0; top: 1178px; width: 900px; height: 94px; background: var(--navy); color: var(--white); font-size: 18.5px; line-height: 26px; letter-spacing: .2px; }
  .footer-address { position: absolute; left: 43px; top: 12px; }
  .footer-contact { position: absolute; right: 40px; top: 12px; text-align: right; }
</style>
</head>
<body>
<div class="stage">
  <div class="flyer-frame">
    <div class="flyer">
      <div class="top-rule"></div>

      <div class="header">
        <svg width="900" height="320" viewBox="0 0 900 320">
          <defs>
            <linearGradient id="hostTone" x1="0" y1="0" x2="1" y2="1">
              <stop offset="0" stop-color="#8d8a83"/>
              <stop offset=".55" stop-color="#b48c74"/>
              <stop offset="1" stop-color="#2c3342"/>
            </linearGradient>
          </defs>
          <rect width="900" height="320" fill="var(--header-grey)"/>
          <polygon points="530,0 900,0 900,320 575,320" fill="url(#hostTone)" role="img" aria-label="Portrait photo of Warren K. Dobbins"/>
        </svg>
        <h1 class="title">Mapping<br>the<br>Mindscape</h1>
      </div>

      <div class="band">
        <p class="band-details">on Tuesday, October 25th<br>at 4 pm in the Halvorsen Auditorium,<br>Drexmoor Center for Applied Discovery</p>
        <div class="host">
          <p class="host-name">Warren K. Dobbins</p>
          <p class="host-role"><span>Professor of Communication in the Feldkamp</span><span>School for Communication and Professor of</span><span>Political Science in the School of Arts &amp; Sciences</span></p>
        </div>
      </div>

      <div class="photo" style="left:51px;top:435px;height:275px;background:linear-gradient(160deg,#eef0f1,#c4a18c 55%,#2e3566);" role="img" aria-label="Portrait photo of Nadine T. Forsyth"></div>
      <p class="speaker-name" style="left:26px;top:720px;">Nadine T. Forsyth</p>
      <p class="speaker-role" style="left:26px;top:749px;">Lewis G. Harlan University Professor<br>(Epigenetics + Biology)</p>

      <p class="feature-note">THIS WILL<br>FEATURE BY<br>FIVE<br>SPEAKERS</p>

      <div class="photo" style="left:603px;top:435px;height:271px;background:linear-gradient(160deg,#4a4f55,#c09a84 55%,#3a3430);" role="img" aria-label="Portrait photo of Tomas Welling"></div>
      <p class="speaker-name" style="left:578px;top:716px;">Tomas Welling</p>
      <p class="speaker-role" style="left:578px;top:745px;">Corinne Fairley University Professor<br>(Mathematics + Systems Engineering)</p>

      <div class="photo" style="left:45px;top:795px;height:271px;background:linear-gradient(160deg,#d7dbdc,#b48a78 55%,#24262a);" role="img" aria-label="Portrait photo of Patrick R. Ellery"></div>
      <p class="speaker-name" style="left:20px;top:1086px;">Patrick R. Ellery</p>
      <p class="speaker-role" style="left:20px;top:1115px;">Martin and Ruth Abelard University Professor<br>(History + Bioethics)</p>

      <div class="photo" style="left:326px;top:795px;height:271px;background:linear-gradient(160deg,#3b3a3c,#d3a892 55%,#eceae6);" role="img" aria-label="Portrait photo of Gordon W. Huxley"></div>
      <p class="speaker-name" style="left:301px;top:1081px;">Gordon W. Huxley</p>
      <p class="speaker-role" style="left:301px;top:1110px;">Thomas E. Wyndel University Professor<br>(Neuroscience + Psychology + Marketing)</p>

      <div class="photo" style="left:603px;top:795px;height:271px;background:linear-gradient(160deg,#6f5f55,#c7957f 55%,#5d6066);" role="img" aria-label="Portrait photo of Colin Tavish"></div>
      <p class="speaker-name" style="left:578px;top:1076px;">Colin Tavish</p>
      <p class="speaker-role" style="left:578px;top:1105px;">Edwin Coyle University Professor<br>(Criminology + Psychiatry + Psychology)</p>

      <div class="footer-rule"></div>
      <footer class="footer">
        <p class="footer-address">Drexmoor Center for Applied Discovery, 1872<br>Larkwell Terrace, Philadelphia, PA 19104.</p>
        <p class="footer-contact">215-555-0147<br>mlok@valdora-univ.example</p>
      </footer>
    </div>
  </div>
</div>
</body>
</html>
```